VALMIK GROUP

This is a company that provides executive protection. Our motto is "New Era in Protection"... I don't want this to look like other security websites. I want it to be clean and sharp and represent a new era. We are based in the bay area so maybe a picture of San Francisco in the background?
I want it to be able to funnel down a couple different categories.
1. About Us
2. Services (Executive Protection, Covert Protection, Residential Protection & Intelligence)
3. Blue Pike (Training & Consulting)
4. Contact Us
I want it to be very clean and modern. I don't want there to be any pictures of bodyguards with ear pieces like every other website.
Target Market(s)
Ultra High Net Worth Individuals
Coding
Coded - Design and coding required
Number of Pages Required
1 page
Requirements
Must have
- Colors of my Symbol
Nice to have
- City in the background, San Francisco, New York or the Thornmeadow Club in Montana.
Should not have
- Should not look like an KVM website or have photos of bodyguards. I want this to be a clean and simple website with my logo

```html
<!DOCTYPE html>
<html lang="en">
<head>
<meta charset="utf-8">
<title>VALMIK GROUP — New Era in Protection</title>
<link href="https://fonts.googleapis.com/css2?family=Orbitron:wght@600;700&family=Poppins:ital,wght@0,400;0,500;0,600;1,400&family=Oswald:wght@400;500&display=swap" rel="stylesheet">
<style>
:root{
  --red:#9b1b1f;
  --red-deep:#6e1014;
  --red-bright:#c0262c;
  --black:#000;
  --ink:#111;
  --white:#fff;
  --footer:#0d0d0d;
  --muted:#cfcfcf;
}
*{margin:0;padding:0;box-sizing:border-box}
html,body{width:1200px;height:3822px;overflow:hidden}
body{position:relative;background:var(--black);font-family:'Poppins',sans-serif;color:var(--white)}
.abs{position:absolute}
.display{font-family:'Orbitron',sans-serif;font-weight:700;letter-spacing:1px}

/* hero */
.hero-photo{left:0;top:0;width:1200px;height:660px;
  background:radial-gradient(ellipse 260px 160px at 880px 150px,#f7b04a 0%,#d9683a 30%,rgba(80,70,110,0) 75%),
  linear-gradient(180deg,#2b3e63 0%,#3d5f8e 22%,#234a78 40%,#1a2f4c 60%,#3a2d22 80%,#1d1712 100%)}
.header-bar{left:0;top:0;width:1200px;height:88px;background:rgba(8,10,18,.82)}
.brand{left:150px;top:22px;font-family:'Orbitron',sans-serif;font-weight:700;font-size:34px;line-height:1;color:var(--white);display:flex;align-items:center;gap:14px}
.brand-mark{width:60px;height:60px;border:4px solid var(--red-bright);border-radius:50%}
.brand small{display:block;font-size:15px;letter-spacing:11px;margin-top:6px}
.top-strip{top:0;height:22px;font-family:'Oswald',sans-serif;font-size:12px;display:flex;align-items:center;padding:0 18px;letter-spacing:.5px}
.strip-mail{left:682px;width:220px;background:var(--red);color:var(--white);clip-path:polygon(0 0,100% 0,92% 100%,4% 100%)}
.strip-phone{left:890px;width:160px;background:var(--white);color:var(--ink);clip-path:polygon(8% 0,100% 0,92% 100%,0 100%);font-weight:500}
.strip-phone svg,.strip-mail svg{margin-right:5px}
.nav{top:56px;left:768px;display:flex;gap:27px;font-family:'Oswald',sans-serif;font-size:13px;letter-spacing:.4px}
.nav a{color:var(--white);text-decoration:none}
.nav a.active{color:var(--red-bright)}

/* intro */
.intro{left:0;top:640px;width:1200px;height:376px;background:var(--red)}
.hero-curve{left:0;top:500px}
.seal{left:495px;top:420px;width:210px;height:210px;border-radius:50%;background:#111;border:10px solid #3a0c0e;display:flex;align-items:center;justify-content:center;font-family:'Poppins',sans-serif;font-weight:600;font-size:20px;letter-spacing:2px;text-align:center;line-height:1.25}
.intro-title{top:676px;left:0;width:1200px;text-align:center;font-size:32px}
.intro-text{top:726px;left:152px;width:896px;text-align:center;font-size:16.5px;line-height:26px;font-weight:500}

/* services */
.services-icon{left:558px;top:971px}
.services-title{top:1074px;left:0;width:1200px;text-align:center;font-size:21px;letter-spacing:2px}
.svc-heading{font-size:22px;color:var(--red-bright);letter-spacing:1.5px}
.svc-text{font-size:16px;line-height:31px;color:var(--white)}
.right{text-align:right}
.checks{list-style:none;font-style:italic;font-size:16px}
.checks li{height:35px;display:flex;align-items:center;gap:14px}
.checks.right li{justify-content:flex-end}
.tick{width:21px;height:21px;flex:none}
.photo-ring{width:350px;height:350px}

/* blue pike */
.pike{left:0;top:2650px;width:1200px;height:568px;background:var(--red)}
.pike-photo{left:150px;top:2683px;width:427px;height:506px;background:linear-gradient(160deg,#e7e9ec 0%,#c9ced4 45%,#8a8f96 75%,#3c3f44 100%)}
.pike-column{left:627px;top:2698px;width:421px;display:flex;flex-direction:column;text-align:right}
.pike-heading{font-size:22px;line-height:28px}
.pike-body{font-size:15.5px;line-height:26px}
.pike-lead{margin-top:10px;text-align:justify;text-align-last:right}
.pike-item{margin-top:12px;padding-top:8px}
.pike-item.ruled{border-top:1px solid rgba(255,255,255,.55)}

/* contact */
.contact{left:0;top:3218px;width:1200px;height:417px;background:var(--white);color:var(--ink)}
.contact-title{top:3268px;left:0;width:1200px;text-align:center;font-size:28px;color:var(--ink)}
.contact-sub{top:3309px;left:0;width:1200px;text-align:center;font-size:14px;font-weight:500;color:var(--ink)}
.field{border:1.5px solid var(--red);border-radius:20px;color:#333;font-size:15px;padding:0 22px;display:flex;align-items:center}
.field.message{border-radius:26px;align-items:flex-start;padding-top:22px}
.submit{left:534px;top:3556px;width:132px;height:36px;border-radius:18px;background:var(--red);color:var(--white);font-size:15px;display:flex;align-items:center;justify-content:center}

/* footer */
.footer{left:0;top:3635px;width:1200px;height:166px;background:var(--footer)}
.foot-brand{left:150px;top:3690px;width:110px;text-align:center;font-family:'Orbitron',sans-serif;font-weight:700;font-size:17px;line-height:1.1;color:var(--white)}
.foot-brand small{display:block;font-size:9px;letter-spacing:5px}
.foot-brand .mark{width:40px;height:40px;border:3px solid var(--red-bright);border-radius:50%;margin:0 auto 6px}
.foot-col{top:3664px;font-size:10px;line-height:17.5px;color:var(--white)}
.foot-col h4{font-family:'Orbitron',sans-serif;font-weight:700;font-size:13px;margin-bottom:4px;letter-spacing:.5px}
.foot-col p{display:flex;align-items:center;gap:5px}
.socials{left:911px;top:3750px;display:flex;gap:9px}
.socials span{width:25px;height:25px;border:1.5px solid var(--white);border-radius:50%}
.copyright{left:0;top:3801px;width:1200px;height:21px;background:var(--red);font-size:9.5px;text-align:center;line-height:21px}
</style>
</head>
<body>

<!-- Hero -->
<div class="abs hero-photo" role="img" aria-label="City skyline at dusk over the bay, lit towers under a sunset sky"></div>
<div class="abs header-bar"></div>
<div class="abs brand"><span class="brand-mark"></span><span>VALMIK<small>GROUP</small></span></div>
<div class="abs top-strip strip-mail">
  <svg width="10" height="10" viewBox="0 0 10 10"><rect x="1" y="2" width="8" height="6" fill="none" stroke="#fff"/><path d="M1 2l4 3 4-3" fill="none" stroke="#fff"/></svg>INFO@VALMIKGROUP.COM</div>
<div class="abs top-strip strip-phone">
  <svg width="10" height="10" viewBox="0 0 10 10"><path d="M2 1l2 2-1 1.2c.6 1.2 1.6 2.2 2.8 2.8L7 6l2 2-1.3 1.3C4.5 9 1 5.5.7 2.3z" fill="#111"/></svg>555-214-0187</div>
<nav class="abs nav"><a href="#">ABOUT US</a><a href="#">SERVICES</a><a href="#" class="active">BLUE PIKE</a><a href="#">CONTACT US</a></nav>

<!-- Intro -->
<div class="abs intro"></div>
<svg class="abs hero-curve" width="1200" height="160" viewBox="0 0 1200 160">
  <path d="M0 155 L470 45 Q600 15 730 45 L1200 120 L1200 160 L0 160 Z" fill="#9b1b1f"/>
</svg>
<div class="abs seal">VALMIK<br>GROUP</div>
<h1 class="abs display intro-title">NEW ERA IN PROTECTION</h1>
<p class="abs intro-text">Lorem ipsum dolor sit amet, consectetur adipiscing elit, sed do eiusmod tempor incididunt ut labore et dolore magna aliqua. Quis ipsum suspendisse ultrices gravida. Risus commodo viverra maecenas accumsan lacus vel facilisis. Lorem ipsum dolor sit amet, consectetur adipiscing elit, sed do eiusmod tempor incididunt ut labore et dolore magna aliqua. Quis ipsum suspendisse ultrices gravida. Risus commodo viverra maecenas accumsan lacus vel facilisis. Lorem ipsum dolor sit amet, consectetur adipiscing elit, sed do eiusmod tempor incididunt ut labore et dolore magna aliqua. Quis ipsum suspendisse ultrices gravida. Risus commodo viverra maecenas accumsan lacus vel facilisis.</p>

<!-- Services -->
<svg class="abs services-icon" width="84" height="84" viewBox="0 0 84 84">
  <circle cx="42" cy="42" r="40" fill="#fff"/>
  <circle cx="42" cy="42" r="34" fill="none" stroke="#9b1b1f" stroke-width="3"/>
  <path d="M42 20l16 6v12c0 11-7 19-16 23-9-4-16-12-16-23V26z" fill="#111"/>
  <circle cx="51" cy="50" r="9" fill="#fff" stroke="#111" stroke-width="2"/>
  <path d="M46.5 50l3 3 5-6" fill="none" stroke="#111" stroke-width="2.2"/>
</svg>
<h2 class="abs display services-title">SERVICES</h2>

<svg width="0" height="0" style="position:absolute">
  <defs>
    <symbol id="tick" viewBox="0 0 21 21"><circle cx="10.5" cy="10.5" r="10.5" fill="#b8232a"/><path d="M5.5 10.8l3.3 3.3 6.5-7" fill="none" stroke="#fff" stroke-width="2.4"/></symbol>
    <symbol id="ring" viewBox="0 0 350 350"><circle cx="175" cy="175" r="168" fill="none" stroke="#fff" stroke-width="12" stroke-dasharray="226 38" stroke-dashoffset="-20"/></symbol>
  </defs>
</svg>

<!-- Executive Protection -->
<h3 class="abs display svc-heading" style="top:1150px;left:519px;width:529px;text-align:right">EXECUTIVE PROTECTION</h3>
<svg class="abs photo-ring" style="left:148px;top:1212px"><use href="#ring"/></svg>
<div class="abs" role="img" aria-label="Uniformed protection officer speaking into a radio" style="left:178px;top:1242px;width:290px;height:290px;border-radius:50%;background:radial-gradient(circle at 50% 35%,#7e8c99,#2c3440 70%,#12161c)"></div>
<p class="abs svc-text right" style="top:1208px;left:519px;width:529px">Lorem ipsum dolor sit amet, consectetur adipiscing elit, sed do eiusmod tempor incididunt ut labore et dolore magna aliqua. Quis ipsum suspendisse ultrices gravida. Risus commodo viverra maecenas accumsan lacus vel facilisis. Lorem ipsum dolor sit amet, consectetur adipiscing elit, sed do eiusmod</p>
<ul class="abs checks right" style="top:1395px;left:519px;width:529px">
  <li>consectetur adipiscing eli<svg class="tick"><use href="#tick"/></svg></li>
  <li>Lorem ipsum dolor sit amet, consectetur adipiscing eli<svg class="tick"><use href="#tick"/></svg></li>
  <li>ipsum dolor sit amet, consectetur adipiscing eli<svg class="tick"><use href="#tick"/></svg></li>
  <li>Lorem ipsum dolor sit amet, consectetur<svg class="tick"><use href="#tick"/></svg></li>
  <li>amet, consectetur adipiscing eli<svg class="tick"><use href="#tick"/></svg></li>
</ul>

<!-- Covert Protection -->
<h3 class="abs display svc-heading" style="top:1636px;left:150px">COVERT PROTECTION</h3>
<p class="abs svc-text" style="top:1685px;left:150px;width:535px">Lorem ipsum dolor sit amet, consectetur adipiscing elit, sed do eiusmod tempor incididunt ut labore et dolore magna aliqua. Quis ipsum suspendisse ultrices gravida. Risus commodo viverra maecenas accumsan lacus vel facilisis. Lorem ipsum dolor sit amet, consectetur adipiscing elit, sed do eiusmod</p>
<ul class="abs checks" style="top:1872px;left:154px;width:540px">
  <li><svg class="tick"><use href="#tick"/></svg>consectetur adipiscing eli</li>
  <li><svg class="tick"><use href="#tick"/></svg>Lorem ipsum dolor sit amet, consectetur adipiscing eli</li>
  <li><svg class="tick"><use href="#tick"/></svg>ipsum dolor sit amet, consectetur adipiscing eli</li>
  <li><svg class="tick"><use href="#tick"/></svg>Lorem ipsum dolor sit amet, consectetur</li>
  <li><svg class="tick"><use href="#tick"/></svg>amet, consectetur adipiscing eli</li>
</ul>
<svg class="abs photo-ring" style="left:695px;top:1694px"><use href="#ring"/></svg>
<div class="abs" role="img" aria-label="Two suited agents beside a black car among green trees" style="left:725px;top:1724px;width:290px;height:290px;border-radius:50%;background:radial-gradient(circle at 50% 30%,#8aa36a,#3f5a2c 55%,#15181a)"></div>

<!-- Intelligence & Consulting -->
<h3 class="abs display svc-heading" style="top:2138px;left:519px;width:529px;text-align:right">INTELLIGENCE &amp; CONSULTING</h3>
<svg class="abs photo-ring" style="left:148px;top:2189px"><use href="#ring"/></svg>
<div class="abs" role="img" aria-label="Hands holding an umbrella over a paper house and family cut-out" style="left:178px;top:2219px;width:290px;height:290px;border-radius:50%;background:radial-gradient(circle at 50% 60%,#e9e9ec,#8d8a95 45%,#3d3a44 80%)"></div>
<p class="abs svc-text right" style="top:2188px;left:519px;width:529px">Lorem ipsum dolor sit amet, consectetur adipiscing elit, sed do eiusmod tempor incididunt ut labore et dolore magna aliqua. Quis ipsum suspendisse ultrices gravida. Risus commodo viverra maecenas accumsan lacus vel facilisis. Lorem ipsum dolor sit amet, consectetur adipiscing elit, sed do eiusmod</p>
<ul class="abs checks right" style="top:2375px;left:519px;width:529px">
  <li>consectetur adipiscing eli<svg class="tick"><use href="#tick"/></svg></li>
  <li>Lorem ipsum dolor sit amet, consectetur adipiscing eli<svg class="tick"><use href="#tick"/></svg></li>
  <li>ipsum dolor sit amet, consectetur adipiscing eli<svg class="tick"><use href="#tick"/></svg></li>
  <li>Lorem ipsum dolor sit amet, consectetur<svg class="tick"><use href="#tick"/></svg></li>
  <li>amet, consectetur adipiscing eli<svg class="tick"><use href="#tick"/></svg></li>
</ul>

<!-- Blue Pike -->
<div class="abs pike"></div>
<div class="abs pike-photo" role="img" aria-label="Trainer presenting at a whiteboard to a seated group"></div>
<div class="abs pike-column">
  <h2 class="display pike-heading">BLUE PIKE</h2>
  <p class="pike-body pike-lead">Lorem ipsum dolor sit amet, consectetur adipiscing elit, sed do eiusmod tempor incididunt ut labore et dolore magna aliqua. Quis ipsum suspendisse ultrices gravida. Risus commodo viverra maecenas accumsan lacus vel facilisis. Lorem ipsum dolor sit amet, consectetur adipiscing elit, sed do eiusmod Lorem ipsum dolor sit amet, consectetur adipiscing elit, sed do eiusmod tempor incididunt ut</p>
  <p class="pike-body pike-item">Lorem ipsum dolor sit amet, consectetur adipiscing elit, sed do eiusmod tempor incididunt ut labore et</p>
  <p class="pike-body pike-item ruled">Lorem ipsum dolor sit amet, consectetur adipiscing tempor incididunt ut labore et dolore magna</p>
  <p class="pike-body pike-item ruled">Lorem ipsum dolor sit amet, consectetur adipiscing tempor incididunt ut labore et dolore magna</p>
</div>

<!-- Contact -->
<div class="abs contact"></div>
<h2 class="abs display contact-title">CONTACT US</h2>
<p class="abs contact-sub">CALL (555) 310-4482 OR FILL OUT THE FORM BELOW.</p>
<div class="abs field" style="left:136px;top:3362px;width:309px;height:37px">Name</div>
<div class="abs field" style="left:466px;top:3362px;width:280px;height:37px">Email</div>
<div class="abs field" style="left:764px;top:3362px;width:301px;height:37px">Phone</div>
<div class="abs field message" style="left:136px;top:3420px;width:929px;height:107px">Message</div>
<div class="abs submit">Contact us</div>

<!-- Footer -->
<div class="abs footer"></div>
<div class="abs foot-brand"><div class="mark"></div>VALMIK<small>GROUP</small></div>
<div class="abs foot-col" style="left:329px"><h4>SERVICES</h4><p>Executive Protection</p><p>Covert Protection</p><p>Residential Protection &amp; Intelligence</p></div>
<div class="abs foot-col" style="left:596px"><h4>PAGES</h4><p>About Us</p><p>Services</p><p>Blue Pike</p><p>Contact Us</p></div>
<div class="abs foot-col" style="left:750px"><h4>ABOUT US</h4><p>Company History</p><p>Our Team</p><p>Certifications</p><p>Careers</p><p>Sitemap</p></div>
<div class="abs foot-col" style="left:911px"><h4>CONTACT</h4>
  <p><svg width="9" height="9" viewBox="0 0 10 10"><path d="M2 1l2 2-1 1.2c.6 1.2 1.6 2.2 2.8 2.8L7 6l2 2-1.3 1.3C4.5 9 1 5.5.7 2.3z" fill="#fff"/></svg>(555) 310-4482</p>
  <p><svg width="9" height="9" viewBox="0 0 10 10"><rect x="0.5" y="2" width="9" height="6" fill="#fff"/><path d="M.5 2l4.5 3 4.5-3" fill="none" stroke="#0d0d0d"/></svg>info@valmikgroup.com</p></div>
<div class="abs socials"><span></span><span></span><span></span></div>
<div class="abs copyright">Copyright © 2021 VALMIK GROUP. All Rights Reserved</div>

</body>
</html>
```